Exec Conference Design Concept

We need to refresh & update nonprofit association graphic design for annual meeting. The graphics will be used to promote the event primarily through digital communications & social media. Other materials we generate for this event are the agenda & billboard content. You can view the existing design at www.lorvamakers.example under Events.

The target audience is primarily male, ages 35-60 in executive positions in C-Corps. The conference topics center on manufacturing regulations, marketing trends, and the economy. This conference has been around almost 30 years so we need something to invigorate potential registrants that will get their attention. It still needs to be professional and business-like.

In addition to a new design concept we would like to update the color palette. We’ve attached some mood boards with potential color & font suggestions. Our company logo is also attached and is the only design element tied to our branding that cannot be changed.

Designs should be energetic and sophisticated. Ideally, we would like the designs in Adobe Indesign or Photoshop. However, we can work with Illustrator.

Target Market(s)

Male business executives age 35-60.

Industry/Entity Type

Polystyrene manufacturing industry supply chain.

Other font styles liked:
• I usually prefer sans serif

Requirements
Must have
• Focus points to draw attention to higher level informational units. For example, some people will only read the headers and not detailed copy.
Nice to have
• Ways to insert bonus content that don’t over power other content. I like to see a good use of white space to enhance readability.

```html
<!DOCTYPE html>
<html lang="en">
<head>
<meta charset="utf-8">
<title>Lorva 2026 Expo</title>
<link rel="stylesheet" href="https://fonts.googleapis.com/css2?family=Fraunces:opsz,wght@9..144,400;9..144,600&family=Figtree:wght@400;500&family=Montserrat:wght@800&display=swap">
<style>
:root{
  --cream:#f6f2ee;
  --amber-top:#c4621c;
  --amber-mid:#dd9a45;
  --rust:#a4521f;
  --rust-deep:#8f4519;
  --title-rust:#9a4a1e;
  --teal:#82a5ae;
  --steel:#4a7a98;
  --ice:#93b9d2;
  --silver:#e6e6e6;
  --gold:#e39a3a;
  --ink:#2b2b2b;
  --white:#ffffff;
  --serif:'Fraunces',Georgia,serif;
  --sans:'Figtree',Arial,sans-serif;
  --display:'Montserrat',Arial,sans-serif;
}
*{margin:0;padding:0;box-sizing:border-box}
html,body{width:1200px;height:4326px;overflow:hidden;background:var(--cream)}
.page{position:relative;width:1200px;height:4326px;font-family:var(--sans);color:var(--ink)}
.abs{position:absolute}
.center{left:0;width:1200px;text-align:center}

.hero-band{top:0;left:0;width:1200px;height:688px;background:radial-gradient(ellipse at 50% 45%,#e8b163 0%,var(--amber-mid) 45%,var(--amber-top) 100%)}
.brand-tile{display:flex;flex-direction:column;align-items:center;justify-content:center;background:#f3ece2;border-radius:12px}
.brand-name{font-family:var(--sans);font-weight:500;color:var(--title-rust);font-size:34px;line-height:1.1;text-align:center}
.brand-url{font-family:var(--sans);font-weight:500;color:var(--title-rust);font-size:11px;margin-top:8px}
.headline{top:200px;font-family:var(--serif);font-weight:600;color:var(--white);font-size:64px;line-height:76px}
.subline{top:438px;color:var(--white);font-size:31px;line-height:43px}

.feature{top:552px;left:149px;width:901px;height:485px;border-radius:12px;overflow:hidden;background:linear-gradient(100deg,var(--steel) 0%,#5d8aa6 55%,#6f93a8 100%)}
.feature-photo{position:absolute;right:0;top:0;width:380px;height:485px;background:linear-gradient(135deg,#dcdcdc 0%,#bcbcbc 60%,#8a9aa4 100%)}
.feature-words{position:absolute;left:94px;top:88px;font-family:var(--display);font-weight:800;font-size:82px;line-height:83px;letter-spacing:2px}
.w-ice{color:var(--ice)}.w-silver{color:var(--silver)}.w-gold{color:var(--gold)}

.section-title{font-family:var(--serif);font-weight:600;color:var(--title-rust);font-size:80px;line-height:90px}
.body-copy{font-size:25px;line-height:36px}

.life-band{top:1400px;left:0;width:1200px;height:535px;background:linear-gradient(180deg,#8eb0b9,var(--teal))}
.life-title{top:1455px;font-family:var(--serif);font-weight:400;color:var(--white);font-size:80px;line-height:94px}
.life-copy{top:1673px;left:175px;width:850px;color:var(--white);text-align:center;font-size:25px;line-height:36px}

.tile{width:433px;height:552px;border-radius:12px}
.tile-build{background:linear-gradient(180deg,#6c9bd0 0%,#b49266 45%,#e8e6e2 100%)}
.tile-pack{background:linear-gradient(135deg,#e8ecef 0%,#6a8fb8 50%,#f2f2f2 100%)}
.tile-green{background:linear-gradient(180deg,#1f3a1c 0%,#5c9a36 45%,#eef0ec 100%)}
.tile-tech{background:linear-gradient(135deg,#f4f5f7 0%,#c4ccd6 55%,#e6e9ee 100%)}
.tile-label{width:433px;text-align:center;font-family:var(--serif);font-size:36px;line-height:43px;color:var(--ink)}

.quote-band{top:3425px;left:0;width:1200px;height:535px;background:radial-gradient(ellipse at 40% 40%,#b96a34,var(--rust) 60%,var(--rust-deep))}
.quote{top:3562px;left:190px;width:820px;text-align:center;font-family:var(--serif);color:var(--white);font-size:36px;line-height:43px}
.quote-by{top:3757px;color:var(--white);font-size:28px}

.contact{display:flex;align-items:center;gap:22px;font-size:28px;line-height:37px;color:var(--ink)}
.icon-dot{width:60px;height:60px;border-radius:50%;background:#9fb9b9;display:flex;align-items:center;justify-content:center;flex:none}
.social{width:62px;height:62px;border-radius:50%;background:#9fb9b9}

.footer-bar{top:4245px;left:0;width:1200px;height:81px;background:var(--rust)}
.copyright{top:4268px;color:var(--white);font-size:26px}
.code-mark{top:4275px;left:1075px;color:var(--white);font-size:17px;font-weight:500}
</style>
</head>
<body>
<main class="page">
  <header>
    <div class="abs hero-band"></div>
    <div class="abs brand-tile" style="top:17px;left:508px;width:182px;height:161px">
      <span class="brand-name">Lorva<br>2026 Expo</span>
      <span class="brand-url">www.lorvamakers.example</span>
    </div>
    <h1 class="abs center headline">Making your life<br>easier, safer and more<br>productive.</h1>
    <p class="abs center subline">Expanded Polystyrene news, knowledge &amp;<br>sustainable solutions.</p>
  </header>

  <section class="abs feature">
    <div class="feature-photo" role="img" aria-label="Close-up of a white expanded polystyrene box corner"></div>
    <div class="feature-words">
      <div class="w-ice">LIGHT</div>
      <div class="w-ice">WEIGHT</div>
      <div class="w-silver">STRONG</div>
      <div class="w-gold">DURABLE</div>
    </div>
  </section>

  <section>
    <h2 class="abs center section-title" style="top:1113px">WHAT IS EPS?</h2>
    <p class="abs body-copy" style="top:1209px;left:170px;width:860px;text-align:center">Expanded Polystyrene (EPS) is a sustainable solution that can be used to keep us warm, safe, and healthy while remaining cost-effective and recyclable. This video offers insights into the world of EPS, highlighting the positive contributions EPS makes in our lives.</p>
  </section>

  <section>
    <div class="abs life-band" role="img" aria-label="Soft-focus photo of medical sample tubes in a lab, tinted teal"></div>
    <h2 class="abs center life-title">TOUCHING YOUR<br>LIFE IN SO MANY WAYS.</h2>
    <p class="abs life-copy">In your home, in your community and in business, state-of-the-art EPS manufacturing technologies create products with reliable performance. EPS delivers fresh food to your dinner table, safely ships important medical treatment and keeps your home and other buildings cooler in the summer and warmer in the winter.</p>
  </section>

  <section>
    <div class="abs tile tile-build" style="top:1970px;left:149px" role="img" aria-label="Construction worker installing EPS insulation panels outdoors"></div>
    <div class="abs tile tile-pack" style="top:1970px;left:614px" role="img" aria-label="Factory worker stacking white EPS packaging boxes"></div>
    <p class="abs tile-label" style="top:2560px;left:149px">BUILDING &amp;<br>CONSTRUCTION</p>
    <p class="abs tile-label" style="top:2560px;left:614px">PACKAGING</p>

    <div class="abs tile tile-green" style="top:2692px;left:149px" role="img" aria-label="Green seedlings growing in a white EPS tray"></div>
    <div class="abs tile tile-tech" style="top:2692px;left:614px" role="img" aria-label="Rolled technical blueprints on a drawing"></div>
    <p class="abs tile-label" style="top:3280px;left:149px">SUSTAINABILITY</p>
    <p class="abs tile-label" style="top:3280px;left:614px">TECHNICAL<br>RESOURCES</p>
  </section>

  <section>
    <div class="abs quote-band" role="img" aria-label="Hands holding a molded EPS part, tinted rust orange"></div>
    <blockquote class="abs quote">“MAKING YOUR LIFE EASIER, SAFER &amp; MORE PRODUCTIVE. WE OFFER EXPANDED POLYSTYRENE NEWS, KNOWLEDGE AND SUSTAINABLE MATERIAL SOLUTIONS.”</blockquote>
    <p class="abs center quote-by">- Lorva Makers Alliance</p>
  </section>

  <footer>
    <div class="abs brand-tile" style="top:3931px;left:830px;width:182px;height:160px">
      <span class="brand-name">Lorva<br>2026 Expo</span>
      <span class="brand-url">www.lorvamakers.example</span>
    </div>
    <div class="abs contact" style="top:4038px;left:149px">
      <span class="icon-dot"><svg width="26" height="30" viewBox="0 0 26 30"><path d="M13 1C6.9 1 2 5.8 2 11.8 2 19.5 13 29 13 29s11-9.5 11-17.2C24 5.8 19.1 1 13 1z" fill="#2f3a3a"/><circle cx="13" cy="11.5" r="4" fill="#9fb9b9"/></svg></span>
      <span>410 Harlow Ave, Ste. 12<br>Brenton, OH 43020</span>
    </div>
    <div class="abs contact" style="top:4132px;left:149px">
      <span class="icon-dot"><svg width="28" height="28" viewBox="0 0 24 24"><path d="M6.6 10.8c1.4 2.8 3.8 5.1 6.6 6.6l2.2-2.2c.3-.3.7-.4 1-.2 1.1.4 2.3.6 3.6.6.6 0 1 .4 1 1V20c0 .6-.4 1-1 1C10.6 21 3 13.4 3 4c0-.6.4-1 1-1h3.5c.6 0 1 .4 1 1 0 1.3.2 2.5.6 3.6.1.3 0 .7-.2 1L6.6 10.8z" fill="#2f3a3a"/></svg></span>
      <span>800-555-0147</span>
    </div>
    <div class="abs social" style="top:4115px;left:825px" aria-label="Social profile"></div>
    <div class="abs social" style="top:4115px;left:894px" aria-label="Social profile"></div>
    <div class="abs social" style="top:4115px;left:964px" aria-label="Social profile"></div>

    <div class="abs footer-bar"></div>
    <p class="abs center copyright">Copyright 2026 Lorva Makers Alliance. All rights reserved.</p>
    <span class="abs code-mark">M1</span>
  </footer>
</main>
</body>
</html>
```